V9 Web Design Project

New company website for Intel cyber security company.

Style should be cool, but remain appropriate for very serious subject matter and audience.

Target Market(s)

Target audience is government and the military

Navigation needs to include:
- About Us
- Services
- Careers
- Contact Us
- Contracts

As well as 2 feature areas - use "Technology Integration" and "Case Study" as the supporting headlines.

Industry/Entity Type

Security

Font styles to use
Sans Serif

Colors

Designer to choose colors to be used in the design.

Requirements
Must have
• Mountain imagery and theme.

Use logo attached.

New Tagline - "Securing the Continuum"
Nice to have
• Supporting imagery could include photos representative of security - avoid cliches.
Should not have
• Needs to be serious not frivolous

```html
<!DOCTYPE html>
<html lang="en">
<head>
<meta charset="utf-8">
<title>V9 Group</title>
<link href="https://fonts.googleapis.com/css2?family=Open+Sans:wght@400;600;700&family=Trocchi&display=swap" rel="stylesheet">
<style>
:root{
  --blue:#3d6fb0;
  --blue-band:#4a7cc2;
  --navy:#1b2a5c;
  --text:#6b6b6b;
  --rule:#d9d9d9;
  --panel:#ffffff;
  --contact-bg:#e7e7e7;
  --dark:#121510;
  --footer-text:#b9bcb6;
}
*{box-sizing:border-box;margin:0;padding:0}
html,body{width:785px;height:1200px;overflow:hidden}
body{position:relative;background:var(--dark);font-family:"Open Sans",Arial,sans-serif;color:var(--text)}
.hero{position:absolute;left:0;top:0;width:785px;height:420px;
  background:linear-gradient(180deg,#3f7f95 0%,#a9b6b0 18%,#d9c6a4 30%,#8ea4b8 45%,#5d6f9a 60%,#2f3a70 78%,#1a1f3a 92%,#121510 100%)}
.hero-title{position:absolute;top:116px;left:0;width:785px;text-align:center;font-family:"Trocchi",Georgia,serif;font-size:26px;font-weight:400;color:var(--navy)}
.slide-arrow{position:absolute;top:208px;width:24px;height:24px;background:rgba(40,40,40,.8);display:flex;align-items:center;justify-content:center}
.slide-arrow.prev{left:0}.slide-arrow.next{right:0}
.site-header{position:absolute;left:70px;top:10px;width:644px;height:56px;background:#fff;border-bottom:3px solid var(--blue)}
.brand{position:absolute;left:8px;top:7px;display:flex;align-items:center;gap:9px}
.brand-mark{width:40px;height:40px;background:var(--navy)}
.brand-name{font-size:21px;font-weight:600;color:var(--navy);line-height:1}
.phone{position:absolute;right:7px;top:11px;font-size:11px;color:var(--blue);display:flex;align-items:center;gap:4px}
.main-nav{position:absolute;right:7px;top:35px;display:flex;gap:26px;font-size:10px;color:#888}
.main-nav .active{color:var(--blue);position:relative}
.main-nav .active::after{content:"";position:absolute;left:-5px;right:-5px;top:19px;height:2px;background:#333}
.content{position:absolute;left:70px;top:398px;width:644px;height:723px;background:var(--panel)}
.welcome{position:absolute;left:0;top:22px;width:644px;text-align:center}
.welcome h2{font-size:18px;font-weight:600;color:var(--blue)}
.welcome p{font-size:9.6px;line-height:16px;margin:6px auto 0;width:570px}
.rule{position:absolute;left:7px;width:627px;height:1px;background:var(--rule)}
.services-intro{position:absolute;left:21px;top:141px;width:190px}
.services-intro h2{font-size:17px;font-weight:600;color:var(--blue)}
.services-intro p{font-size:9.6px;line-height:16.1px;margin-top:8px}
.btn-outline{position:absolute;left:2px;top:236px;width:87px;height:33px;border:1px solid var(--blue);color:var(--blue);font-size:12px;display:flex;align-items:center;justify-content:center}
.service-tile{position:absolute;width:192px;height:122px}
.service-tile .photo{height:91px}
.service-tile .label{height:31px;background:var(--blue-band);color:#fff;font-size:10.5px;font-weight:600;padding:9px 12px}
.partners{position:absolute;left:8px;top:480px;width:628px;display:flex;justify-content:space-between;align-items:center;font-size:12px;color:#8a8a8a;font-weight:600}
.contact{position:absolute;left:7px;top:519px;width:630px;height:195px;background:var(--contact-bg)}
.contact h2{text-align:center;font-size:22px;font-weight:600;color:var(--blue);margin-top:16px}
.field{position:absolute;background:#fff;border:1px solid #d5d5d5;border-radius:2px;font-size:8.5px;color:#888;padding:5px 9px}
.submit{position:absolute;left:291px;top:149px;width:50px;height:21px;background:#6f6f6f;border-radius:2px;color:#fff;font-size:9.5px;font-weight:600;display:flex;align-items:center;justify-content:center}
.site-footer{position:absolute;left:71px;top:1140px;font-size:8.8px;color:var(--footer-text)}
.site-footer nav{display:flex;gap:5px}
.site-footer p{margin-top:10px}
.social{position:absolute;left:639px;top:1147px;display:flex;gap:5px}
.social span{width:21px;height:21px;border-radius:50%}
</style>
</head>
<body>
<section class="hero" role="img" aria-label="Snow-capped mountain range under a golden sky, fading into dark forest"></section>
<h1 class="hero-title">Technology Integration &amp; Case Study</h1>
<div class="slide-arrow prev"><svg width="12" height="12" viewBox="0 0 12 12"><path d="M10 6H2M6 2L2 6l4 4" stroke="#fff" stroke-width="2" fill="none"/></svg></div>
<div class="slide-arrow next"><svg width="12" height="12" viewBox="0 0 12 12"><path d="M2 6h8M6 2l4 4-4 4" stroke="#fff" stroke-width="2" fill="none"/></svg></div>

<header class="site-header">
  <div class="brand">
    <div class="brand-mark"></div>
    <div class="brand-name">V9 Group</div>
  </div>
  <div class="phone"><svg width="9" height="9" viewBox="0 0 24 24"><path fill="currentColor" d="M6.6 10.8a15 15 0 006.6 6.6l2.2-2.2c.3-.3.7-.4 1-.2 1.1.4 2.3.6 3.6.6.6 0 1 .4 1 1V20c0 .6-.4 1-1 1A17 17 0 013 4c0-.6.4-1 1-1h3.5c.6 0 1 .4 1 1 0 1.3.2 2.5.6 3.6.1.3 0 .7-.2 1z"/></svg>555 014 2290</div>
  <nav class="main-nav"><span class="active">About Us</span><span>Services</span><span>Careers</span><span>Contact Us</span><span>Contracts</span></nav>
</header>

<main class="content">
  <section class="welcome">
    <h2>WELCOME TO V9 GROUP</h2>
    <p>Mauris efficitur nisi risus, eget malesuada augue ultricies quis. Quisque ultricies tempus tellus, et tempus nisi maximus ac. Praesent varius nisl sed feugiat vehicula. Quisque hendrerit, nisi a cursus auctor, tellus metus dignissim mi, a scelerisque augue mauris ut nibh. Curabitur tempus interdum risus et tristique. Cum sociis natoque penatibus et magnis dis.</p>
  </section>
  <div class="rule" style="top:116px"></div>

  <section class="services-intro">
    <h2>OUR SERVICES</h2>
    <p>Aliquam erat volutpat. Quisque condimen-tum scelerisque mauris, consequat blandit arcu aliquet quis. Pellentesque et ipsum elit. Cras eu faucibus massa. Integer interdum justo non ante mattis fermentum sed venenatis nisi. Etiam molestie tortor id lacinia fermentum. Integer dapibus pellentesque felis, ut posuere nunc aliquam eu. Cras turpis arcu, sagittis ac dolor eu, interdum tempus est. Etiam risus sem, consequat id laoreet eu, scelerisque in dui.</p>
    <div class="btn-outline">Get Started</div>
  </section>

  <div class="service-tile" style="left:231px;top:144px">
    <div class="photo" role="img" aria-label="Analyst at a keyboard in front of streaming code" style="background:linear-gradient(135deg,#1c2c5a,#3a5c94 50%,#0f1830)"></div>
    <div class="label">PRAESENT MALESUADA</div>
  </div>
  <div class="service-tile" style="left:444px;top:144px">
    <div class="photo" role="img" aria-label="Close-up of an eye scan with digital overlay" style="background:linear-gradient(135deg,#8a2a1a,#d6a58e 50%,#e9e3dc)"></div>
    <div class="label">SUSPENDISSE COMMODO</div>
  </div>
  <div class="service-tile" style="left:231px;top:287px">
    <div class="photo" role="img" aria-label="Padlock icons on a digital tablet" style="background:linear-gradient(135deg,#6e6e72,#2a2a2e 55%,#15151a)"></div>
    <div class="label">MAECENAS VIVERRA SIT</div>
  </div>
  <div class="service-tile" style="left:444px;top:287px">
    <div class="photo" role="img" aria-label="Hand holding a glowing globe amid threat labels" style="background:linear-gradient(135deg,#3a3a3a,#3b6fc4 50%,#1a1a1a)"></div>
    <div class="label">QUISQUE ULTRICIES</div>
  </div>

  <div class="rule" style="top:438px"></div>

  <div class="partners">
    <span>Hollow Lane</span><span>Brightmesh</span><span>Relayhub</span><span>Ledgerly</span><span>Korvane</span><span>NTX</span><span>Quantova</span><span>Arcline</span><span>Netrion</span>
  </div>

  <section class="contact">
    <h2>CONTACT US</h2>
    <div class="field" style="left:49px;top:55px;width:170px;height:22px">Name</div>
    <div class="field" style="left:231px;top:55px;width:170px;height:22px">E-mail</div>
    <div class="field" style="left:412px;top:55px;width:170px;height:22px">Phone</div>
    <div class="field" style="left:49px;top:90px;width:533px;height:42px">Details</div>
    <div class="submit">SUBMIT</div>
  </section>
</main>

<footer class="site-footer">
  <nav><span>Home</span>|<span>About Us</span>|<span>Services</span>|<span>Careers</span>|<span>Contact Us</span>|<span>Contracts</span></nav>
  <p>Copyright © 2014 V9Group. All rights reserved.</p>
</footer>
<div class="social"><span style="background:#3b5a9a"></span><span style="background:#2aa3e0"></span><span style="background:#6ab04c"></span></div>
</body>
</html>
```